Hadley & Partners, LLC Business Card 2016

We need a new business card design for a very important trade show coming up.

We are a compliance Consulting Firm. Our clients are stock brokerage firms and investment advisers.

I would like our logo on both sides of the card.

Info in the front of the card shold include:

Logo
First & Last Name
Title
Office #
Cell #
Email
Company Address (42 W. Calloway St., Suite 300 Pasadena, CA 91417

Back of the card should include the logo and url: www.hadleypartnersgroup.com

Target Market(s)

Stock Brokerage Firms and Investment Advisers

Industry/Entity Type

Financial Service

Contact Information for Business Card

Marcus J. Pellew
President
42 W. Calloway St., Suite 300
Pasadena, CA 91417
O 626.555.0147 ext. 204
C 818.555.0193
Email: marcus@hadleypartnersgroup.com
www.hadleypartnersgroup.com

Requirements
Nice to have
• The back of the card could be black with the logo with the white letters.
• I do want the front of the card to at least have the color logo with the black "Hadley & Partners Lettering.

```html
<!DOCTYPE html>
<html lang="en">
<head>
<meta charset="utf-8">
<title>Hadley &amp; Partners — Business Card</title>
<link rel="stylesheet" href="https://fonts.googleapis.com/css2?family=Open+Sans:wght@400;600;700&display=swap">
<style>
  :root {
    --backdrop: #e7e4e1;
    --card-black: #1b1b1c;
    --card-edge: #262627;
    --accent-red: #c0272d;
    --text-white: #f2f2f2;
    --text-grey: #a3a3a5;
    --divider: #6b6b6d;
  }
  * { margin: 0; padding: 0; box-sizing: border-box; }
  html, body { width: 1200px; height: 864px; overflow: hidden; }
  body {
    background: var(--backdrop);
    font-family: "Open Sans", Arial, sans-serif;
    position: relative;
  }
  .card {
    position: absolute;
    width: 560px;
    height: 320px;
    background: linear-gradient(160deg, var(--card-edge), var(--card-black) 60%);
    border-radius: 4px;
    box-shadow: 0 10px 28px rgba(0,0,0,.28);
    color: var(--text-white);
  }
  .brand {
    display: flex;
    align-items: center;
    gap: 12px;
  }
  .brand-square {
    background: var(--accent-red);
    flex: none;
  }
  .brand-name {
    font-weight: 600;
    color: var(--text-white);
    white-space: nowrap;
  }

  /* Back of card */
  .card-back { left: 50px; top: 70px; }
  .card-back .brand { position: absolute; left: 130px; top: 100px; }
  .card-back .brand-square { width: 34px; height: 34px; }
  .card-back .brand-name { font-size: 28px; letter-spacing: .5px; }
  .card-back .site-url {
    position: absolute;
    left: 44px; bottom: 54px;
    font-size: 13px;
    letter-spacing: 3px;
    color: var(--text-grey);
  }

  /* Front of card */
  .card-front { left: 590px; top: 420px; }
  .card-front .brand { position: absolute; left: 26px; top: 136px; gap: 8px; }
  .card-front .brand-square { width: 18px; height: 18px; }
  .card-front .brand-name { font-size: 17px; }
  .card-front .divider {
    position: absolute;
    left: 252px; top: 34px;
    width: 1px; height: 252px;
    background: linear-gradient(to bottom, transparent, var(--divider) 25%, var(--divider) 75%, transparent);
  }
  .contact { position: absolute; left: 270px; top: 40px; right: 18px; }
  .person-name { font-size: 19px; font-weight: 700; color: var(--accent-red); line-height: 1.2; }
  .person-title { font-size: 14px; margin-top: 2px; }
  .address { font-size: 12.5px; line-height: 1.4; margin-top: 8px; color: var(--text-white); }
  .contact-list { list-style: none; margin-top: 16px; }
  .contact-list li {
    display: flex; align-items: center; gap: 8px;
    font-size: 12.5px; line-height: 1; margin-bottom: 9px;
  }
  .contact-list svg { width: 13px; height: 13px; flex: none; fill: var(--accent-red); }
</style>
</head>
<body>

<section class="card card-back" aria-label="Card back">
  <div class="brand">
    <span class="brand-square"></span>
    <span class="brand-name">Hadley &amp; Partners</span>
  </div>
  <p class="site-url">www.hadleypartnersgroup.com</p>
</section>

<section class="card card-front" aria-label="Card front">
  <div class="brand">
    <span class="brand-square"></span>
    <span class="brand-name">Hadley &amp; Partners</span>
  </div>
  <div class="divider"></div>
  <div class="contact">
    <p class="person-name">Marcus J. Pellew</p>
    <p class="person-title">President</p>
    <p class="address">42 W. Calloway St., Suite 300<br>Pasadena, CA 91417</p>
    <ul class="contact-list">
      <li>
        <svg viewBox="0 0 16 16" aria-hidden="true"><path d="M3 1h3l1.5 4-2 1.3a9 9 0 0 0 4.2 4.2L11 8.5l4 1.5v3a2 2 0 0 1-2 2A13 13 0 0 1 1 3a2 2 0 0 1 2-2z"/></svg>
        626.555.0147 ext. 204
      </li>
      <li>
        <svg viewBox="0 0 16 16" aria-hidden="true"><path d="M4.5 0h7A1.5 1.5 0 0 1 13 1.5v13a1.5 1.5 0 0 1-1.5 1.5h-7A1.5 1.5 0 0 1 3 14.5v-13A1.5 1.5 0 0 1 4.5 0zM5 2v10h6V2zm3 11a1 1 0 1 0 0 2 1 1 0 0 0 0-2z"/></svg>
        818.555.0193
      </li>
      <li>
        <svg viewBox="0 0 16 16" aria-hidden="true"><path d="M1 3h14v10H1zm1.5 1.2V5l5.5 4 5.5-4v-.8z"/></svg>
        marcus@hadleypartnersgroup.com
      </li>
      <li>
        <svg viewBox="0 0 16 16" aria-hidden="true"><circle cx="8" cy="8" r="7"/></svg>
        www.hadleypartnersgroup.com
      </li>
    </ul>
  </div>
</section>

</body>
</html>
```